Corporate-Design für Handwerks- und Dienstleistungsfirma
Erster Vorschlag Logo hat mich nicht mehr losgelassen. Meine Wünsche wurden sehr schnell erfasst und umgesetzt, Top Service Besten Dank!
Zielgruppe
Ich gründe eine Einzelfirma und biete Dienstleistungen im Bereich Handwerk jeglicher Art, mit Schwerpunkt Holz. Zielgruppe Privatpersonen, Verwaltungen etc.
Aufgabenstellung
Den Namen Handwerk und Dienstleistung sollen im Vordergrund stehen, Name, Telefon, E Mail eher Zweitrangig, muss aber bei einem Einzelunternehmen aufgeführt werden.

```html
<!DOCTYPE html>
<html lang="de">
<head>
<meta charset="utf-8">
<title>Hubert Melk – Handwerk &amp; Dienstleistung</title>
<link rel="stylesheet" href="https://fonts.googleapis.com/css2?family=Ubuntu:wght@400;700&family=Bree+Serif&family=Oswald:wght@400&display=swap">
<style>
  :root {
    --green: #3dab35;
    --charcoal: #47474b;
    --stage-light: #f7f7f7;
    --paper: #ffffff;
    --ink: #1d1d1d;
    --signature-blue: #1f5fae;
  }
  * { margin: 0; padding: 0; box-sizing: border-box; }
  html, body { width: 1200px; height: 2402px; overflow: hidden; }
  body { position: relative; background: var(--charcoal); font-family: "Ubuntu", sans-serif; color: var(--ink); }

  .brand-stage { position: absolute; left: 0; top: 0; width: 1200px; height: 672px; background: var(--stage-light); }
  .brand-mark {
    position: absolute; display: flex; flex-direction: column; align-items: center; justify-content: center;
    font-family: "Ubuntu", sans-serif; font-weight: 700; color: var(--green); text-align: center; line-height: 1.1;
  }
  .brand-mark .dot { border-radius: 50%; background: var(--green); }
  .brand-stage .brand-mark { left: 0; top: 0; width: 1200px; height: 672px; font-size: 64px; }
  .brand-stage .brand-mark .dot { width: 40px; height: 40px; margin-bottom: 24px; }

  .card { position: absolute; top: 737px; width: 372px; height: 241px; box-shadow: 18px 22px 30px rgba(0,0,0,.35); }
  .card-front { left: 196px; background: var(--paper); }
  .card-front .brand-mark { inset: 0; font-size: 26px; }
  .card-front .brand-mark .dot { width: 16px; height: 16px; margin-bottom: 10px; }
  .card-back { left: 634px; background: var(--green); }

  .contact { font-family: "Oswald", sans-serif; color: var(--paper); text-align: center; }
  .contact .phone { font-size: 30px; letter-spacing: -1px; line-height: 1.1; }
  .contact .email { font-size: 14px; line-height: 1.2; }
  .card-back .contact { position: absolute; left: 0; right: 0; top: 96px; }

  .letter { position: absolute; left: 142px; top: 1032px; width: 920px; height: 1301px; background: var(--paper); box-shadow: 22px 26px 36px rgba(0,0,0,.4); }
  .letter .brand-mark { left: 660px; top: 38px; width: 200px; height: 180px; font-size: 26px; }
  .letter .brand-mark .dot { width: 16px; height: 16px; margin-bottom: 10px; }
  .letter-band { position: absolute; left: 648px; top: 238px; width: 272px; height: 87px; background: var(--green); }
  .letter-band .contact { position: absolute; left: 24px; top: 18px; text-align: left; }
  .letter-band .phone { font-size: 28px; }

  .sender-line { position: absolute; left: 94px; top: 192px; width: 390px; padding-bottom: 3px; border-bottom: 1px solid #555; font-family: "Bree Serif", serif; font-size: 14px; color: #444; }
  .recipient { position: absolute; left: 115px; top: 238px; font-size: 20px; line-height: 29px; letter-spacing: .3px; }
  .recipient .city { margin-top: 26px; }

  .letter-body { position: absolute; left: 115px; top: 518px; width: 690px; font-size: 20.5px; line-height: 28.3px; letter-spacing: .2px; }
  .letter-body .salutation { margin-bottom: 28px; }
  .letter-body p + p { margin-top: 10px; }
  .letter-body .closing { margin-top: 26px; }
  .signature { display: block; width: 310px; height: 40px; margin-top: 18px; background: linear-gradient(90deg, rgba(31,95,174,.35), rgba(31,95,174,.12)); border-radius: 20px; }
</style>
</head>
<body>
  <section class="brand-stage">
    <div class="brand-mark"><span class="dot"></span>Hubert Melk</div>
  </section>

  <div class="card card-front">
    <div class="brand-mark"><span class="dot"></span>Hubert Melk</div>
  </div>
  <div class="card card-back">
    <div class="contact">
      <div class="phone">+41 79 555 12 34</div>
      <div class="email">melk.hubert@postfeld.example</div>
    </div>
  </div>

  <article class="letter">
    <div class="brand-mark"><span class="dot"></span>Hubert Melk</div>
    <div class="letter-band">
      <div class="contact">
        <div class="phone">+41 79 555 12 34</div>
        <div class="email">melk.hubert@postfeld.example</div>
      </div>
    </div>

    <div class="sender-line">Hubert Melk | Beispielstrassse 123 | 54321 Musterstadt</div>
    <address class="recipient" style="font-style:normal">
      <div>Lorem ipsum dolor</div>
      <div>consectetuer adipiscing elit</div>
      <div>autem vel eum 123</div>
      <div class="city">54321 consequat</div>
    </address>

    <div class="letter-body">
      <p class="salutation">Lorem ipsum dolor sit,</p>
      <p>amet, consectetuer adipiscing elit, sed diam nonummy nibh euismod tincidunt ut laoreet dolore magna aliquam erat volut&shy;pat. Ut wisi enim ad minim veniam, quis nostrud exerci tation ullamcorper suscipit lobortis nisl ut aliquip ex ea commodo consequat.</p>
      <p>Duis autem vel eum iriure dolor in hendrerit in vulputate velit esse molestie consequat, vel illum dolore eu feugiat nulla facili&shy;sis at vero eros et accumsan et iusto odio dignissim qui blandit nulla facilisi.</p>
      <p>Lorem ipsum dolor sit amet, cons ectetuer adipiscing elit, sed diam nonummy nibh euismod tincidunt ut laoreet dolore magna nostrud exerci tation ullamcorper suscipit lobortis nisl ut aliquip ex ea commodo consequat.</p>
      <p>Dolor sit amet, consectetuer adipiscing elit, sed diam nonummy nibh euismod tincidunt ut laoreet dolore magna nostrud exerci tation ullamcorper suscipit lobortis nisl ut aliquip ex ea commo&shy;do consequat.</p>
      <p class="closing">Duis autem vel eum</p>
      <span class="signature" role="img" aria-label="Handschriftliche Unterschrift in Blau"></span>
    </div>
  </article>
</body>
</html>
```